Marketing Thornbury

We are a primary school and would like to market our school in a positive light. We have had recent success and would like the local community to know!

Target Market(s)

Parents/Carers in the local community

Industry/Entity Type

School

Font styles to use
Serif

Requirements
Must have
• Thornbury Logo first with our moto 'Opening Minds Side by Side'

Reference to the fact we are converting to academy status on 1st April 2014 with The Harrowby BRIDGE Academy Trust

Reference to the partnership with Caldwick Primary School which has bought recent, quick success

Reference to Edvisor rating of Good. Feb 2014
Nice to have
• School colours dark red

Link to website www.thornburyprimary.example

Link to the academy website www.harrowbybridge.example

Statements from Edvisor -

'This is a good school'

'The Executive Headteacher and leadership team have skilfully steered the school's recovery and galvanised staff at all levels to work as a team'

'This is a very different school to the one that existed at the time of the previous inspection'

'Pupils achievement has improved very quickly this year'

'Pupils make a strong start in the school'

'The quality of teaching is good'

'The behaviour of pupils is good'

```html
<!DOCTYPE html>
<html lang="en">
<head>
<meta charset="utf-8">
<title>Thornbury Primary School</title>
<link rel="stylesheet" href="https://fonts.googleapis.com/css2?family=Noto+Serif:wdth,wght@62.5..100,400..900&family=Playfair+Display+SC:wght@700;900&display=swap">
<style>
  :root {
    --frame-red: #d0202a;
    --frame-blue: #3aa0dc;
    --header-green: #72c05e;
    --title-gold: #f6b92c;
    --title-edge: #c9241d;
    --tagline-blue: #2c7fd0;
    --crest-red: #7c1618;
    --grad-top: #fde468;
    --grad-mid: #e9893a;
    --grad-low: #d8492c;
    --grad-end: #cf2a2a;
    --wall-top: #e8532b;
    --wall-bottom: #d9262a;
    --rosette: #d9652a;
    --tick: #e0202a;
    --text-light: #ffffff;
  }
  * { margin: 0; padding: 0; box-sizing: border-box; }
  html, body { width: 932px; height: 1200px; overflow: hidden; background: #fff; }
  .poster {
    position: relative; width: 932px; height: 1200px; background: #fff;
    font-family: "Noto Serif", Georgia, serif;
  }
  .frame-outer { position: absolute; inset: 3px; border: 3px solid var(--frame-red); }
  .frame-inner { position: absolute; inset: 10px; border: 2px solid var(--frame-blue); }
  .canvas {
    position: absolute; left: 14px; top: 14px; right: 14px; bottom: 14px; overflow: hidden;
    background: linear-gradient(150deg, var(--grad-top) 0%, var(--grad-mid) 40%, var(--grad-low) 70%, var(--grad-end) 100%);
  }
  .header-band {
    position: absolute; left: 5px; top: 3px; right: 5px; height: 98px;
    background: var(--header-green); border-radius: 4px;
    display: flex; align-items: center; justify-content: center;
  }
  .school-title {
    font-family: "Playfair Display SC", Georgia, serif; font-weight: 900;
    font-size: 44px; letter-spacing: 1px; color: var(--title-gold);
    -webkit-text-stroke: 1.2px var(--title-edge);
    text-shadow: 2px 3px 3px rgba(120,40,0,0.45);
  }
  .crest {
    position: absolute; left: 32px; top: 104px; width: 103px; height: 102px;
    background: var(--crest-red); display: flex; align-items: center; justify-content: center;
    color: var(--text-light); font-weight: 700; font-size: 16px;
  }
  .tagline {
    position: absolute; left: 160px; top: 128px; width: 740px; text-align: center;
    font-weight: 900; font-size: 30px; text-transform: uppercase; letter-spacing: 1px;
    color: var(--tagline-blue); -webkit-text-stroke: 0.8px #0d3f7a;
    text-shadow: 1px 2px 2px rgba(0,0,0,0.35);
  }
  .note, .quote, .address-block, .web-links {
    position: absolute; color: var(--text-light); font-weight: 700; white-space: nowrap;
    font-stretch: 72%; font-variation-settings: "wdth" 72;
    text-shadow: 1px 1px 1px rgba(120,40,0,0.35);
  }
  .note { font-size: 21px; line-height: 27px; letter-spacing: 0.3px; }
  .note-partnership { left: 196px; top: 250px; }
  .note-academy { left: 188px; top: 327px; }
  .note-rating { left: 188px; top: 410px; font-size: 22px; }
  .note sup { font-size: 11px; }
  .rosette { position: absolute; width: 68px; height: 90px; }
  .rosette-one { left: 104px; top: 233px; }
  .rosette-two { left: 104px; top: 329px; }
  .quote { font-size: 22px; line-height: 26px; letter-spacing: 0.3px; }
  .quote-lead { left: 137px; top: 500px; }
  .q1 { left: 140px; top: 540px; }
  .q2 { left: 138px; top: 657px; }
  .q3 { left: 136px; top: 729px; }
  .q4 { left: 140px; top: 792px; }
  .q5 { left: 140px; top: 840px; }
  .tick { position: absolute; width: 58px; height: 34px; left: 64px; }
  .t1 { top: 556px; } .t2 { top: 672px; } .t3 { top: 747px; } .t4 { top: 803px; } .t5 { top: 850px; }
  .wall {
    position: absolute; left: 0; right: 0; top: 918px; bottom: 0;
    background: linear-gradient(180deg, var(--wall-top), var(--wall-bottom));
  }
  .address-block {
    left: 534px; top: 924px; font-stretch: 100%; font-variation-settings: "wdth" 100;
    font-weight: 900; font-size: 21px; line-height: 32.5px; letter-spacing: 0.4px;
  }
  .web-links { left: 40px; top: 1085px; font-size: 20px; line-height: 30px; }
</style>
</head>
<body>
<div class="poster">
  <div class="frame-outer"></div>
  <div class="frame-inner"></div>
  <div class="canvas">
    <header class="header-band"><h1 class="school-title">Thornbury Primary School</h1></header>
    <div class="crest">Thornbury</div>
    <p class="tagline">Opening Minds Side by Side</p>

    <svg class="rosette rosette-one" viewBox="0 0 68 90" aria-hidden="true">
      <path d="M22 40 L10 84 L22 76 L30 88 L36 48 Z M40 44 L48 86 L54 74 L64 80 L50 40 Z" fill="var(--rosette)" stroke="#9a3a16" stroke-width="1"/>
      <circle cx="32" cy="28" r="24" fill="var(--rosette)" stroke="#b34a1b" stroke-width="2" stroke-dasharray="3 2"/>
      <circle cx="32" cy="28" r="16" fill="var(--rosette)"/>
    </svg>
    <p class="note note-partnership">Our partnership with Caldwick Primary School<br>has brought recent, quick success.</p>

    <svg class="rosette rosette-two" viewBox="0 0 68 90" aria-hidden="true">
      <path d="M22 40 L10 84 L22 76 L30 88 L36 48 Z M40 44 L48 86 L54 74 L64 80 L50 40 Z" fill="var(--rosette)" stroke="#9a3a16" stroke-width="1"/>
      <circle cx="32" cy="28" r="24" fill="var(--rosette)" stroke="#b34a1b" stroke-width="2" stroke-dasharray="3 2"/>
      <circle cx="32" cy="28" r="16" fill="var(--rosette)"/>
    </svg>
    <p class="note note-academy">We are converting to academy status on 1<sup>st</sup> April 2014<br>with The Harrowby BRIDGE Academy Trust.</p>

    <p class="note note-rating">Edvisor rating: Good &mdash; February 2014</p>

    <p class="quote quote-lead">This is a good school.</p>

    <svg class="tick t1" viewBox="0 0 58 34" aria-hidden="true"><path d="M2 16 L20 32 L56 2 L22 22 Z" fill="var(--tick)" stroke="#8a1010" stroke-width="1"/></svg>
    <p class="quote q1">The Executive Headteacher and leadership team have<br>skilfully steered the school's recovery and galvanised<br>staff at all levels to work as a team.</p>

    <svg class="tick t2" viewBox="0 0 58 34" aria-hidden="true"><path d="M2 16 L20 32 L56 2 L22 22 Z" fill="var(--tick)" stroke="#8a1010" stroke-width="1"/></svg>
    <p class="quote q2">This is a very different school to the one that existed<br>at the time of the previous inspection.</p>

    <svg class="tick t3" viewBox="0 0 58 34" aria-hidden="true"><path d="M2 16 L20 32 L56 2 L22 22 Z" fill="var(--tick)" stroke="#8a1010" stroke-width="1"/></svg>
    <p class="quote q3">Pupils' achievement has improved very quickly<br>this year.</p>

    <svg class="tick t4" viewBox="0 0 58 34" aria-hidden="true"><path d="M2 16 L20 32 L56 2 L22 22 Z" fill="var(--tick)" stroke="#8a1010" stroke-width="1"/></svg>
    <p class="quote q4">Pupils make a strong start in the school.</p>

    <svg class="tick t5" viewBox="0 0 58 34" aria-hidden="true"><path d="M2 16 L20 32 L56 2 L22 22 Z" fill="var(--tick)" stroke="#8a1010" stroke-width="1"/></svg>
    <p class="quote q5">The quality of teaching is good.<br>The behaviour of pupils is good.</p>

    <div class="wall" role="img" aria-label="Red brick wall texture"></div>
    <p class="web-links">www.thornburyprimary.example<br>www.harrowbybridge.example</p>
    <address class="address-block" style="font-style:normal">
      Thornbury Primary School<br>
      Linden way<br>
      Great Hollowmere<br>
      Marlowfield<br>
      Eastshire<br>
      Telephone:&nbsp; 01632 960412<br>
      fax :01632 960587
    </address>
  </div>
</div>
</body>
</html>
```